New Business Card Design Project

Hi! I would like for you to design a business card for our aesthetic injections business. We offer Zelvia, filler, skin care. I would like it to be elegant, feminine, modern and sleek/clean. I like black/gold foil/ivory/parchment colors. It can be either one or two sided. I would like matte black with gold foil logo on one side and ivory with gold foil information on the other side

Target Market(s)

target market is the discerning woman who wants to look her best

Industry/Entity Type

beauty

Contact Information for Business Card

logo, name, phone, email, website, instagram, facebook, location

Requirements
Must have
• logo and info
Nice to have
• the icons for cell, instagram, email, fb etc
Should not have
• images of people

```html
<!DOCTYPE html>
<html lang="en">
<head>
<meta charset="UTF-8">
<title>Velour Room – Business Card</title>
<link rel="stylesheet" href="https://fonts.googleapis.com/css2?family=Lato:wght@400;700&family=Oswald:wght@600&display=swap">
<style>
  :root {
    --backdrop: #1c1c1e;
    --card: #0f1011;
    --gold: #d8c69a;
    --gold-deep: #b59f6c;
    --ivory: #f4f1ea;
    --rule: #6c6658;
  }
  * { margin: 0; padding: 0; box-sizing: border-box; }
  html, body {
    width: 1200px; height: 900px; overflow: hidden;
    background: var(--backdrop);
  }
  .canvas {
    position: relative; width: 1200px; height: 900px;
  }
  .card {
    position: absolute; left: 320px;
    width: 560px; height: 320px;
    background: var(--card);
    box-shadow: 0 14px 30px rgba(0,0,0,.55);
    overflow: hidden;
  }
  .card--front { top: 70px; }
  .card--back { top: 490px; }
  .card__band {
    position: absolute; left: 0; right: 0; bottom: 0; height: 10px;
    background: linear-gradient(90deg, var(--gold-deep), var(--gold), var(--gold-deep));
  }

  /* Front: brand mark */
  .brand {
    position: absolute; left: 50%; top: 40px;
    width: 200px; height: 200px; margin-left: -100px;
    border: 1.5px solid var(--gold);
    border-radius: 50%;
    display: flex; align-items: center; justify-content: center;
  }
  .brand__name {
    font-family: "Lato", sans-serif; font-weight: 400;
    font-size: 26px; letter-spacing: 3px;
    color: var(--gold); text-align: center; line-height: 1.25;
  }

  /* Back: contact details */
  .person {
    position: absolute; left: 40px; top: 110px; width: 230px;
    text-align: right;
  }
  .person__name {
    font-family: "Oswald", sans-serif; font-weight: 600;
    font-size: 30px; letter-spacing: .5px; color: var(--gold);
    text-transform: uppercase; line-height: 1.1;
  }
  .person__role {
    font-family: "Lato", sans-serif; font-size: 15px;
    color: var(--ivory); margin-top: 4px;
  }
  .divider {
    position: absolute; left: 292px; top: 108px;
    width: 1px; height: 80px; background: var(--rule);
  }
  .contact {
    position: absolute; left: 312px; top: 112px;
    list-style: none;
    font-family: "Lato", sans-serif; font-size: 15px; color: var(--ivory);
  }
  .contact__item {
    display: flex; align-items: center; gap: 9px; height: 25px;
  }
  .contact__icon { width: 15px; height: 15px; flex: none; }
  .address {
    position: absolute; left: 40px; bottom: 32px;
    font-family: "Lato", sans-serif; font-size: 15px; color: var(--ivory);
  }
</style>
</head>
<body>
<main class="canvas">

  <section class="card card--front" aria-label="Card front">
    <div class="brand">
      <p class="brand__name">VELOUR<br>ROOM</p>
    </div>
    <div class="card__band"></div>
  </section>

  <section class="card card--back" aria-label="Card back">
    <div class="person">
      <h1 class="person__name">Marcus Hale</h1>
      <p class="person__role">Managing Director</p>
    </div>
    <div class="divider"></div>
    <ul class="contact">
      <li class="contact__item">
        <svg class="contact__icon" viewBox="0 0 24 24" fill="none" stroke="var(--gold)" stroke-width="2" stroke-linecap="round" stroke-linejoin="round">
          <path d="M22 16.9v3a2 2 0 0 1-2.2 2 19.8 19.8 0 0 1-8.6-3.1 19.5 19.5 0 0 1-6-6A19.8 19.8 0 0 1 2.1 4.2 2 2 0 0 1 4.1 2h3a2 2 0 0 1 2 1.7c.1.9.4 1.8.7 2.7a2 2 0 0 1-.5 2.1L8 9.8a16 16 0 0 0 6 6l1.3-1.3a2 2 0 0 1 2.1-.4c.9.3 1.8.6 2.7.7a2 2 0 0 1 1.7 2z"/>
        </svg>
        044-987 654 321
      </li>
      <li class="contact__item">
        <svg class="contact__icon" viewBox="0 0 24 24" fill="none" stroke="var(--gold)" stroke-width="2" stroke-linejoin="round">
          <rect x="2" y="5" width="20" height="14"/>
          <path d="M2 5l10 8 10-8"/>
        </svg>
        hello@velourroom.com
      </li>
      <li class="contact__item">
        <svg class="contact__icon" viewBox="0 0 24 24" fill="none" stroke="var(--gold)" stroke-width="2">
          <circle cx="12" cy="12" r="10"/>
          <path d="M2 12h20M12 2c3 3 4 6.5 4 10s-1 7-4 10c-3-3-4-6.5-4-10s1-7 4-10z"/>
        </svg>
        www.velourroom.com
      </li>
    </ul>
    <p class="address">18 Linden Row, Harbor City, 30817</p>
    <div class="card__band"></div>
  </section>

</main>
</body>
</html>
```